Wedding Invitations

We are a printing company "inkmakers" and require multiple wedding invitation designs for our customers in store and online. We would like the designs to be editable in Photoshop if possible, if not then a layout with suggested fonts would be the next best option. We are open to suggestions on design but would like to stick to the general wedding themes some with a modern and some with a classical feel

Industry/Entity Type

Printing

```html
<!DOCTYPE html>
<html lang="en">
<head>
<meta charset="utf-8">
<title>Wedding Invitation – Eleanor and Samuel</title>
<link rel="stylesheet" href="https://fonts.googleapis.com/css2?family=Josefin+Slab:wght@300;400&family=Quicksand:wght@300;400&display=swap">
<style>
  :root {
    --paper: #98f97c;
    --ink: #111511;
    --monogram: #5b6866;
    --muted: #6e8273;
    --blossom-light: #c9fbf4;
    --blossom-mid: #a9f0c6;
  }
  html, body {
    margin: 0;
    padding: 0;
    overflow: hidden;
    background: var(--paper);
  }
  .invitation {
    position: relative;
    width: 880px;
    height: 1200px;
    overflow: hidden;
    background: var(--paper);
    color: var(--ink);
    font-family: "Quicksand", "Helvetica Neue", Arial, sans-serif;
    font-weight: 300;
    text-align: center;
  }
  .blossom-art {
    position: absolute;
    left: 0;
    top: 730px;
    width: 880px;
    height: 470px;
  }
  .line {
    position: absolute;
    left: 0;
    width: 100%;
    margin: 0;
    white-space: nowrap;
  }
  .monogram {
    top: 56px;
    font-family: "Josefin Slab", Georgia, serif;
    font-weight: 300;
    font-size: 136px;
    line-height: 1;
    color: var(--monogram);
    letter-spacing: -4px;
  }
  .hosts {
    top: 274px;
    font-size: 32px;
    line-height: 40px;
  }
  .hosts .amp {
    display: block;
    font-size: 22px;
    line-height: 40px;
  }
  .request {
    top: 422px;
    font-size: 26px;
    line-height: 32px;
    color: var(--muted);
  }
  .couple {
    top: 556px;
    font-family: "Josefin Slab", Georgia, serif;
    font-weight: 400;
    font-size: 86px;
    line-height: 1;
  }
  .details {
    top: 724px;
    font-size: 26px;
    line-height: 31px;
  }
  .details p {
    margin: 0;
  }
  .details .time {
    margin-top: 31px;
  }
  .details .venue {
    margin-top: 37px;
  }
</style>
</head>
<body>
<main class="invitation">
  <svg class="blossom-art" viewBox="0 0 880 470" role="img" aria-label="Soft watercolour blossom clusters in pale mint and aqua drifting across the lower part of the card">
    <defs>
      <radialGradient id="blossom-left" cx="0.5" cy="0.5" r="0.5">
        <stop offset="0" stop-color="var(--blossom-light)" stop-opacity="0.85"/>
        <stop offset="0.55" stop-color="var(--blossom-mid)" stop-opacity="0.5"/>
        <stop offset="1" stop-color="var(--blossom-mid)" stop-opacity="0"/>
      </radialGradient>
      <radialGradient id="blossom-right" cx="0.5" cy="0.5" r="0.5">
        <stop offset="0" stop-color="var(--blossom-light)" stop-opacity="0.8"/>
        <stop offset="0.55" stop-color="var(--blossom-mid)" stop-opacity="0.45"/>
        <stop offset="1" stop-color="var(--blossom-mid)" stop-opacity="0"/>
      </radialGradient>
    </defs>
    <ellipse cx="200" cy="220" rx="220" ry="210" fill="url(#blossom-left)"/>
    <ellipse cx="700" cy="300" rx="220" ry="130" fill="url(#blossom-right)"/>
  </svg>

  <h1 class="line monogram">ES</h1>

  <p class="line hosts">
    Gordon and Marian Pryce
    <span class="amp">&amp;</span>
    Martin and Caroline Ashby
  </p>

  <p class="line request">Request the honor of your presence<br>at the marriage of their children</p>

  <h2 class="line couple">Eleanor and Samuel</h2>

  <div class="line details">
    <p class="date">Saturday the fourteenth of September<br>Two thousand and thirteen</p>
    <p class="time">4 o’clock in the afternoon</p>
    <p class="venue">Willow Pond Garden<br>in Linden Park<br>Brookhaven, New York</p>
  </div>
</main>
</body>
</html>
```